eBook Cover_H. Vollmar-Tessen
Schnell und zuverlässoig,Änderungswünsche wurden umgehend ausgeführt. Vielen Dank für das tolle Cover zu meinem ersten Buch!
Zielgruppe
freie Roman-Autorin (Erstlingswerk)
Zielgruppe: Lesende (Erwachsene), Frauen
Charakterisierung: magisch-realistischer Familienroman, spielt im Europa der Jetzt-Zeit
Aufgabenstellung
Im ersten Schritt geht es um ein Cover für ein eBook, das aber bei Bedarf als Book on Demand gedruckt werden soll. Es wird daher später Anforderung bzgl. Dicke / Umfang des gedruckten Buches und einer Rückseite geben. Das gewählte Design soll dann dahingehend überarbeitet und finale Druckdaten zur Verfügung gestellt werden. Dies soll von vornherein berücksichtigt werden und im Preis enthalten sein.
Titel: Nebel über Glas, Funken im Moor
Autorinnenname: Henrike Vollmar-Tessen
des weiteren auf dem Cover: Roman

```html
<!DOCTYPE html>
<html lang="de">
<head>
<meta charset="utf-8">
<title>Nebel über Glas, Funken im Moor – Henrike Vollmar-Tessen</title>
<link rel="stylesheet" href="https://fonts.googleapis.com/css2?family=Parisienne&family=Source+Sans+3:wght@600;700&display=swap">
<style>
  :root {
    --page-bg: #dcdcdc;
    --sky-blue: #2899c4;
    --signal-red: #c81113;
    --circle-white: #ffffff;
    --circle-rim: #e27a7c;
    --text-white: #ffffff;
    --field-deep: #27379a;
    --field-green: #7fbb35;
    --field-yellow: #cdc63c;
    --field-poppy: #e0231c;
  }
  html, body {
    margin: 0;
    padding: 0;
    width: 841px;
    height: 1200px;
    overflow: hidden;
    background: var(--page-bg);
  }
  .book-cover {
    position: absolute;
    left: 45px;
    top: 45px;
    width: 750px;
    height: 1108px;
    background: var(--sky-blue);
    box-shadow: 6px 6px 6px rgba(0,0,0,0.35);
    overflow: hidden;
  }
  .cover-shapes {
    position: absolute;
    inset: 0;
    width: 750px;
    height: 1108px;
  }
  .author-name {
    position: absolute;
    top: 80px;
    left: 0;
    width: 100%;
    margin: 0;
    text-align: center;
    font-family: "Parisienne", cursive;
    font-weight: 400;
    font-size: 46px;
    line-height: 60px;
    color: var(--text-white);
    letter-spacing: 0.5px;
  }
  .author-rule {
    position: absolute;
    top: 163px;
    left: 145px;
    width: 455px;
    height: 3px;
    background: var(--text-white);
  }
  .book-title {
    position: absolute;
    top: 218px;
    left: 0;
    width: 100%;
    margin: 0;
    text-align: center;
    font-family: "Source Sans 3", sans-serif;
    font-weight: 700;
    font-size: 68px;
    line-height: 79px;
    letter-spacing: 1.5px;
    color: var(--text-white);
  }
  .book-title span { display: block; }
  .genre-badge {
    position: absolute;
    left: 220px;
    top: 628px;
    width: 302px;
    height: 302px;
    box-sizing: border-box;
    border-radius: 50%;
    background: var(--circle-white);
    border: 4px solid var(--circle-rim);
    display: flex;
    align-items: center;
    justify-content: center;
  }
  .genre-label {
    display: inline-block;
    font-family: "Source Sans 3", sans-serif;
    font-weight: 600;
    font-size: 70px;
    line-height: 1;
    color: var(--signal-red);
    transform: scaleX(0.9);
  }
</style>
</head>
<body>
  <div class="book-cover">
    <svg class="cover-shapes" viewBox="0 0 750 1108" xmlns="http://www.w3.org/2000/svg">
      <defs>
        <linearGradient id="field-gradient" x1="0" y1="0" x2="0" y2="1">
          <stop offset="0" stop-color="var(--field-deep)"/>
          <stop offset="0.35" stop-color="var(--field-deep)"/>
          <stop offset="0.5" stop-color="var(--field-green)"/>
          <stop offset="0.72" stop-color="var(--field-yellow)"/>
          <stop offset="0.9" stop-color="var(--field-green)"/>
          <stop offset="1" stop-color="var(--field-poppy)"/>
        </linearGradient>
      </defs>
      <polygon class="red-wedge" points="0,384 750,661 0,895" fill="var(--signal-red)"/>
      <polygon class="painted-meadow" role="img" aria-label="Gemalte Mohnwiese unter dunkelblauem Himmel"
               points="0,895 750,661 750,1108 0,1108" fill="url(#field-gradient)"/>
    </svg>

    <p class="author-name">Henrike Vollmar-Tessen</p>
    <div class="author-rule"></div>
    <h1 class="book-title"><span>Nebel über Glas</span><span>Funken im Moor</span></h1>
    <div class="genre-badge"><span class="genre-label">ROMAN</span></div>
  </div>
</body>
</html>
```